I need creative and unique business card design using my company logo. Ok to change logo color. We are a small brokerage doing both Real Estate and Mortgage services. Need to have the follow on business card;
1. agent name - Mila Fenton - Realtor
2. cell - 949-555-0182
3. license number - DRE 04917362
4. business name - Brightway Estates & Lending, Inc
5. business office - 626-555-0147
6. business address - 287 W. Larkmoor Ave #214, Arcadia CA 91088
7. business logo - attached (ok to use different color on logo)

```html
<!DOCTYPE html>
<html lang="en">
<head>
<meta charset="utf-8">
<title>Mila Fenton – Business Card</title>
<link href="https://fonts.googleapis.com/css2?family=Montserrat:wght@400;500;700&display=swap" rel="stylesheet">
<style>
  :root{
    --bg:#1c1c1c;
    --paper:#f3f3f3;
    --brand:#2b57a6;
    --brand-deep:#1f4690;
    --brand-light:#5a8fd0;
    --band-dark:rgba(20,52,118,.55);
    --band-light:rgba(140,185,235,.35);
    --ink:#333333;
    --white:#ffffff;
  }
  *{box-sizing:border-box;margin:0;padding:0}
  html,body{width:1200px;height:1059px;overflow:hidden;background:var(--bg);font-family:"Montserrat",sans-serif}
  .card{position:absolute;border-radius:18px;overflow:hidden}
  .card-front{left:257px;top:89px;width:687px;height:390px;background:var(--paper)}
  .card-back{left:254px;top:547px;width:693px;height:393px;background:var(--brand)}

  .brand-block{position:absolute;left:37px;top:37px;width:182px}
  .brand-square{width:92px;height:92px;background:var(--brand);margin:0 auto}
  .brand-name{margin-top:17px;color:var(--brand);font-weight:500;font-size:13.5px;letter-spacing:2.2px;line-height:1.4;text-transform:uppercase;text-align:center}

  .agent{position:absolute;right:37px;top:54px;text-align:right;color:var(--ink)}
  .agent-name{color:var(--brand);font-weight:700;font-size:27px;letter-spacing:1px;line-height:1}
  .agent-role{font-size:17px;margin-top:3px;line-height:1.15}
  .agent-license{font-size:17px;margin-top:0;line-height:1.2}
  .agent-license .label{color:var(--brand)}
  .accent-bar{position:absolute;right:0;top:56px;width:23px;height:59px;background:var(--brand)}

  .address{position:absolute;left:38px;top:222px;font-size:17px;line-height:23px;color:var(--ink);font-style:normal}
  .contacts{position:absolute;left:38px;top:283px;list-style:none;font-size:17px;color:var(--ink)}
  .contacts li{display:flex;align-items:center;height:25.5px}
  .contacts svg{width:12px;height:12px;margin-right:8px;fill:var(--brand)}

  .back-tone{position:absolute;inset:0;background:linear-gradient(90deg,var(--brand-deep) 0%,var(--brand) 50%,var(--brand-light) 100%)}
  .back-bands{position:absolute;inset:0;
    background:
      repeating-linear-gradient(180deg,transparent 0 0px,transparent 0 29px,rgba(255,255,255,0) 29px 29px),
      linear-gradient(90deg,var(--band-dark) 0%,rgba(30,70,140,.4) 55%,var(--band-light) 100%);
    -webkit-mask:repeating-linear-gradient(180deg,#000 0 41px,transparent 41px 70.5px);
            mask:repeating-linear-gradient(180deg,#000 0 41px,transparent 41px 70.5px)}
  .back-fade{position:absolute;inset:0;background:linear-gradient(180deg,rgba(255,255,255,.06) 0%,rgba(0,0,0,.08) 100%)}
  .back-brand{position:absolute;left:583px;top:281px;width:47px;height:47px;background:var(--white)}
  .back-name{position:absolute;right:124px;top:296px;color:var(--white);font-weight:500;font-size:13px;letter-spacing:1.6px;text-transform:uppercase;line-height:17px}
</style>
</head>
<body>
  <section class="card card-front">
    <div class="brand-block">
      <div class="brand-square"></div>
      <div class="brand-name">Brightway Estates<br>&amp; Lending, Inc</div>
    </div>

    <div class="agent">
      <div class="agent-name">MILA FENTON</div>
      <div class="agent-role">Realtor</div>
      <div class="agent-license"><span class="label">Lic No</span> - DRE 04917362</div>
    </div>
    <div class="accent-bar"></div>

    <address class="address">287 W. Larkmoor Ave #214<br>Arcadia CA 91088</address>

    <ul class="contacts">
      <li><svg viewBox="0 0 24 24"><path d="M2 9c0-3 4-5 10-5s10 2 10 5v2h-5V8.5c-1.5-.6-3.2-.9-5-.9s-3.5.3-5 .9V11H2zM5 13h14l2 8H3z"/></svg>626-555-0147</li>
      <li><svg viewBox="0 0 24 24"><path d="M7 1h10a2 2 0 0 1 2 2v18a2 2 0 0 1-2 2H7a2 2 0 0 1-2-2V3a2 2 0 0 1 2-2zm0 3v14h10V4z"/></svg>949-555-0182</li>
      <li><svg viewBox="0 0 24 24"><path d="M2 9l10-7 10 7v13H2zm2 2v9h16v-9l-8 6z"/></svg>Mila.fenton@brightmail.com</li>
    </ul>
  </section>

  <section class="card card-back">
    <div class="back-tone"></div>
    <div class="back-bands" role="img" aria-label="Rows of a repeating tonal brand pattern across the card back"></div>
    <div class="back-fade"></div>
    <div class="back-name">Brightway Estates &amp; Lending, Inc</div>
    <div class="back-brand"></div>
  </section>
</body>
</html>
```